Design Wexbo Ads for Pantrova

Market Overview:

The food safety management system market is highly competitive, with many systems offering comprehensive features that go beyond basic food logging. These systems often include functionalities such as workplace safety, staff management, and advanced food labelling.

Pantrova Differentiation:

Pantrova stands out in this crowded market due to its simplicity and affordability. Unlike many competitors, Pantrova focuses exclusively on essential food safety tasks, making it an ideal solution for small food-based businesses. These are businesses that typically rely on pen and paper for minimal recording of temperatures, food logs, delivery logs, and simple task management.

Target Audience:

Pantrova is designed for small food-based businesses that need an efficient, cost-effective solution for basic food safety and logging tasks. These businesses are not looking for comprehensive systems that include workplace safety, staff management, or advanced food labelling. Instead, they need a straightforward tool to transition from manual record-keeping to a digital solution without incurring high costs.

Key Benefits:

Cost-Effective: Pantrova is significantly cheaper than many competitors because it focuses solely on essential food safety functions.

User-Friendly: The simplicity of Pantrova makes it easy for small businesses to implement and use without extensive training or support.

Targeted Solution: By concentrating on basic food safety tasks, Pantrova provides exactly what small food-based businesses need, avoiding the complexity and expense of more comprehensive systems.

This focus on affordability, simplicity, and targeted functionality makes Pantrova the perfect solution for small food businesses looking to improve their food safety management without the added cost and complexity of larger systems.
We want some Wexbo Display Ads.

Wexbo Display Ad Sizes:
300x250
336x280
300x600
728x90
160x600
Ad Title: The Restaurant Food Safety App

Brand: Pantrova

Main Line:
The Restaurant Food Safety App

Key Points:
Streamline HACCP Audits
Eliminate Paperwork

Call to Action (CTA):
Start Your Free Trial Today

Visual Elements:
Pantrova Logo prominently displayed
Clean, modern design emphasising simplicity and efficiency
Visuals of the app in use, highlighting key features like audit streamlining and paperless operation

Tone:
Professional, efficient, and user-friendly

Target Audience:
Restaurant owners and managers
Food safety compliance officers

Objective:
Highlight the app's capability to streamline food safety audits and reduce paperwork
Encourage potential users to start a free trial

Ad Title: Ditch Paperwork, Streamline Food Safety

Brand: Pantrova

Main Line:
Ditch Paperwork, Streamline Food Safety

Key Points:
Easy to Use
HACCP Approved

Call to Action (CTA):

Visual Elements:
Clean, modern design emphasising ease of use and HACCP approval
Visuals showcasing the simplicity and effectiveness of the app

Tone:
Professional, straightforward, and efficient

Target Audience:

Objective:
Highlight the app's user-friendliness and HACCP approval

TIP: Submit one design and if you are selected you can then design the other ratios of ads keeping the exact same design.

Target Market(s)

Restaurants & Cafe Owners

Industry/Entity Type

Hospitality

Requirements
Must have
• Pantrova Logo Main copy line and CTA
Nice to have
• Main copy Line I but in brief and the key points
Should not have
• Ugly design

```html
<!DOCTYPE html>
<html lang="en">
<head>
<meta charset="utf-8">
<title>Pantrova Display Ads – 300 x 250</title>
<link href="https://fonts.googleapis.com/css2?family=Bebas+Neue&family=Montserrat:wght@600;700;800&family=Poppins:wght@500;600;700;800&family=Yellowtail&display=swap" rel="stylesheet">
<style>
  :root {
    --board: #8eabd6;
    --navy: #0d1628;
    --navy-deep: #0a1120;
    --teal: #36c2c9;
    --teal-soft: #7fd8dc;
    --white: #ffffff;
    --ink: #111318;
    --paper: #eff0f1;
    --ring-grey: #e2e3e5;
  }
  * { box-sizing: border-box; margin: 0; padding: 0; }
  html, body { width: 1200px; height: 615px; overflow: hidden; }
  body {
    background: var(--board);
    position: relative;
    font-family: "Poppins", sans-serif;
  }
  .size-label {
    position: absolute;
    top: 56px;
    width: 475px;
    text-align: center;
    color: var(--white);
    font-family: "Poppins", sans-serif;
    font-weight: 500;
    font-size: 23px;
  }
  .banner {
    position: absolute;
    top: 110px;
    width: 475px;
    height: 395px;
    overflow: hidden;
    box-shadow: 0 18px 22px -12px rgba(40, 60, 100, 0.45);
  }
  .abs { position: absolute; }

  /* ---------- Dark banner ---------- */
  .banner--dark {
    left: 110px;
    background: radial-gradient(circle at 30% 70%, #0f3a46 0%, var(--navy) 45%, var(--navy-deep) 100%);
  }
  .banner--dark .brand {
    left: 0; right: 0; top: 30px;
    text-align: center;
    color: var(--white);
    font-family: "Poppins", sans-serif;
    font-weight: 700;
    font-size: 40px;
  }
  .headline-top {
    left: 0; right: 0; top: 100px;
    text-align: center;
    color: var(--teal);
    font-family: "Montserrat", sans-serif;
    font-weight: 700;
    font-size: 22px;
  }
  .headline-main {
    left: 0; right: 0; top: 126px;
    text-align: center;
    color: var(--white);
    font-family: "Bebas Neue", sans-serif;
    font-size: 48px;
    letter-spacing: 0.2px;
    line-height: 1;
  }
  .perks {
    left: 32px; top: 193px;
    list-style: none;
    color: var(--white);
    font-family: "Montserrat", sans-serif;
    font-weight: 600;
    font-size: 18px;
    line-height: 21px;
  }
  .perks li { display: flex; align-items: flex-start; gap: 13px; margin-bottom: 6px; }
  .perks svg { flex: none; margin-top: 1px; }
  .cta-top {
    left: 48px; top: 297px;
    width: 130px; height: 27px;
    background: var(--teal);
    color: var(--white);
    font-family: "Montserrat", sans-serif;
    font-weight: 800;
    font-size: 17px;
    line-height: 27px;
    text-align: center;
  }
  .cta-bottom {
    left: 34px; top: 321px;
    width: 172px; height: 32px;
    background: var(--white);
    color: var(--navy);
    font-family: "Montserrat", sans-serif;
    font-weight: 700;
    font-size: 17px;
    line-height: 32px;
    text-align: center;
    transform: rotate(-3deg);
  }
  .devices-dark {
    left: 188px; top: 223px;
    width: 278px; height: 150px;
    border-radius: 6px;
    background: linear-gradient(90deg, #e9edf2 0%, #dfe5ec 45%, #1b2433 60%, #141c29 100%);
  }

  /* ---------- Light banner ---------- */
  .banner--light {
    left: 616px;
    background: var(--paper);
  }
  .banner--light .brand {
    left: 24px; top: 26px;
    color: var(--ink);
    font-family: "Poppins", sans-serif;
    font-weight: 700;
    font-size: 42px;
  }
  .tag-the {
    left: 24px; top: 93px;
    width: 61px; height: 34px;
    background: var(--teal);
    color: var(--white);
    font-family: "Poppins", sans-serif;
    font-weight: 800;
    font-size: 22px;
    line-height: 36px;
    text-align: center;
    border-radius: 3px;
  }
  .title-line {
    left: 26px;
    font-family: "Poppins", sans-serif;
    font-weight: 800;
    line-height: 1;
  }
  .title-restaurant { top: 124px; font-size: 24px; color: var(--ink); letter-spacing: -0.3px; }
  .title-food { top: 149px; font-size: 44px; color: var(--teal); }
  .title-safety { top: 192px; font-size: 31px; color: var(--ink); left: 29px; }
  .title-app {
    top: 222px; left: 28px;
    font-family: "Yellowtail", cursive;
    font-size: 40px;
    color: var(--ink);
    line-height: 1;
  }
  .points {
    left: 26px; top: 274px;
    list-style: none;
    font-family: "Poppins", sans-serif;
    font-weight: 600;
    font-size: 14px;
    color: var(--ink);
  }
  .points li { display: flex; align-items: center; gap: 12px; height: 24px; }
  .cta-light {
    left: 27px; top: 334px;
    width: 220px; height: 37px;
    background: var(--teal);
    color: var(--white);
    font-family: "Poppins", sans-serif;
    font-weight: 700;
    font-size: 15px;
    line-height: 37px;
    text-align: center;
  }
  .probe {
    left: 278px; top: 18px;
    width: 70px; height: 300px;
    border-radius: 10px;
    background: linear-gradient(180deg, #dfe9ee 0%, #f6f8f9 50%, #c9d2d6 100%);
  }
  .tablet {
    left: 288px; top: 232px;
    width: 145px; height: 170px;
    border-radius: 10px;
    background: linear-gradient(180deg, #2fa9b0 0%, #1a2535 12%, #101826 100%);
  }
</style>
</head>
<body>

  <div class="size-label" style="left:110px">300 x 250 banner</div>
  <div class="size-label" style="left:616px">300 x 250 banner</div>

  <!-- Dark banner -->
  <section class="banner banner--dark">
    <svg class="abs" width="475" height="395" viewBox="0 0 475 395" aria-hidden="true">
      <circle cx="98" cy="94" r="12" fill="var(--white)"/>
      <circle cx="282" cy="199" r="7" fill="var(--white)"/>
      <circle cx="0" cy="157" r="21" fill="var(--teal)"/>
      <circle cx="478" cy="52" r="20" fill="var(--teal)"/>
      <circle cx="245" cy="220" r="21" fill="var(--teal)"/>
      <path d="M300 395 C300 330 330 226 420 220 C460 217 475 225 475 225 L475 395 Z" fill="var(--teal)"/>
    </svg>

    <div class="abs brand">Pantrova</div>
    <div class="abs headline-top">DITCH PAPERWORK,</div>
    <div class="abs headline-main">STREAMLINE FOOD SAFETY</div>

    <ul class="abs perks">
      <li>
        <svg width="17" height="17" viewBox="0 0 24 24"><path fill="var(--teal)" d="M2 10h4v12H2zM8 22V10l5-8c2 0 3 1 2.5 3L14 9h6c1.5 0 2.5 1.4 2 2.8l-3 8.6c-.3 1-1.2 1.6-2.2 1.6z"/></svg>
        <span>EASY TO USE</span>
      </li>
      <li>
        <svg width="17" height="17" viewBox="0 0 24 24"><path fill="var(--teal)" d="M2 10h4v12H2zM8 22V10l5-8c2 0 3 1 2.5 3L14 9h6c1.5 0 2.5 1.4 2 2.8l-3 8.6c-.3 1-1.2 1.6-2.2 1.6z"/></svg>
        <span>HACCP<br>APPROVED</span>
      </li>
    </ul>

    <div class="abs devices-dark" role="img" aria-label="Laptop, phone and tablet showing the app's temperature logs, with a probe thermometer"></div>

    <div class="abs cta-top">START YOUR</div>
    <div class="abs cta-bottom">FREE TRIAL TODAY</div>
  </section>

  <!-- Light banner -->
  <section class="banner banner--light">
    <svg class="abs" width="475" height="395" viewBox="0 0 475 395" aria-hidden="true">
      <circle cx="453" cy="28" r="38" fill="none" stroke="var(--ring-grey)" stroke-width="10"/>
      <path d="M262 0 H362 V162 A50 50 0 0 1 262 162 Z" fill="var(--navy)"/>
      <circle cx="255" cy="166" r="42" fill="none" stroke="var(--teal-soft)" stroke-width="12"/>
      <path d="M362 214 A49 49 0 0 1 460 214 V395 H362 Z" fill="var(--teal)"/>
    </svg>

    <div class="abs probe" role="img" aria-label="Handheld probe thermometer with digital display"></div>
    <div class="abs tablet" role="img" aria-label="Tablet showing the app's food safety log screen"></div>

    <div class="abs brand">Pantrova</div>
    <div class="abs tag-the">THE</div>
    <div class="abs title-line title-restaurant">RESTAURANT</div>
    <div class="abs title-line title-food">FOOD</div>
    <div class="abs title-line title-safety">SAFETY</div>
    <div class="abs title-app">App</div>

    <ul class="abs points">
      <li>
        <svg width="16" height="16" viewBox="0 0 16 16"><circle cx="8" cy="8" r="8" fill="var(--teal)"/><path d="M4.5 8.2l2.3 2.2 4.6-4.6" fill="none" stroke="var(--white)" stroke-width="1.8"/></svg>
        <span>Streamline HACCP Audits</span>
      </li>
      <li>
        <svg width="16" height="16" viewBox="0 0 16 16"><circle cx="8" cy="8" r="8" fill="var(--teal)"/><path d="M4.5 8.2l2.3 2.2 4.6-4.6" fill="none" stroke="var(--white)" stroke-width="1.8"/></svg>
        <span>Eliminate Paperwork</span>
      </li>
    </ul>

    <div class="abs cta-light">Start Your Free Trial Today</div>
  </section>

</body>
</html>
```